Weekly Newsletter template for our niche within the Telecom Industry

We need a 'skeleton' format where we can insert our weekly information and ads.
We will do all the content in-house.
Content in both info and ads must be able to contain hyperlinks.
Our company website is: www. halverd-quenby.com
We think we would like something similar to the top format but with the single bar on the right side as a place to insert ads
Thank you.

```html
<!DOCTYPE html>
<html lang="en">
<head>
<meta charset="utf-8">
<title>Halverd Quenby Weekly Newsletter</title>
<link href="https://fonts.googleapis.com/css2?family=Mulish:wght@400;600;700;800&display=swap" rel="stylesheet">
<style>
  :root {
    --teal: #2b9aa0;
    --olive: #b3c040;
    --news-bg: #bdc94b;
    --text: #5a5a5a;
    --ink: #1c1c1c;
    --rule-warm: #8c6a72;
    --footer: #000000;
    --white: #ffffff;
  }
  * { box-sizing: border-box; margin: 0; padding: 0; }
  html, body { width: 692px; height: 1200px; overflow: hidden; background: var(--white); }
  body { font-family: "Mulish", Arial, sans-serif; color: var(--text); }
  .newsletter { position: relative; width: 692px; height: 1200px; border-top: 4px solid var(--teal); }
  .newsletter::before { content: ""; position: absolute; left: 0; right: 0; top: 0; height: 1px; background: var(--olive); }

  .brand { position: absolute; left: 43px; top: 36px; display: flex; align-items: center; gap: 12px; }
  .brand-dot { width: 40px; height: 40px; border-radius: 50%; background: var(--teal); }
  .brand-name { font-weight: 800; font-size: 24px; letter-spacing: 1px; color: var(--ink); line-height: 1; }

  .site-pill { position: absolute; left: 394px; top: 35px; width: 255px; height: 43px; border-radius: 22px;
    background: linear-gradient(90deg, var(--olive), var(--teal) 45%, #4aa79a 80%, var(--olive));
    display: flex; align-items: center; gap: 14px; padding-left: 2px; color: var(--white);
    font-weight: 700; font-size: 13.5px; text-decoration: none; }
  .site-pill .globe { width: 39px; height: 39px; border-radius: 50%; background: var(--olive);
    display: flex; align-items: center; justify-content: center; }

  .main-col { position: absolute; left: 43px; top: 127px; width: 337px; }
  .heading { color: var(--teal); font-weight: 800; font-size: 15px; line-height: 21.6px; text-transform: uppercase; }
  .body-text { font-size: 12.6px; line-height: 23.4px; text-align: justify; }
  .main-col .heading + .body-text { margin-top: 4px; }
  .main-col .heading.second { margin-top: 16px; }
  .sub-heading { color: var(--olive); font-weight: 800; font-size: 14px; line-height: 22px; margin-top: 7px; }
  .main-col .sub-heading + .body-text { margin-top: 8px; }
  .main-col .body-text.next { margin-top: 12px; }
  .callout { margin-top: 22px; padding: 10px 0 15px; border-top: 1px solid var(--rule-warm); border-bottom: 1px solid var(--teal);
    color: var(--olive); font-weight: 800; font-size: 12.8px; line-height: 23.4px; text-align: justify; }

  .news-box { position: absolute; left: 405px; top: 132px; width: 245px; height: 363px; background: var(--news-bg);
    padding: 24px 22px 0 24px; color: var(--white); }
  .news-title { font-weight: 800; font-size: 19.5px; margin-bottom: 8px; }
  .news-item { font-size: 10.8px; font-weight: 600; line-height: 21.6px; margin-bottom: 21px; }
  .news-item a { color: inherit; text-decoration: none; }

  .feature-art { position: absolute; left: 405px; top: 522px; width: 245px; height: 229px; overflow: hidden;
    background: radial-gradient(circle at 55% 35%, #9fd0e8 0%, #3a6e93 35%, #13263d 75%),
                linear-gradient(#1a2e48, #0e1a2a); }
  .feature-art::after { content: ""; position: absolute; inset: 0;
    background: radial-gradient(ellipse at 30% 80%, rgba(255,150,80,.55), transparent 45%); }

  .faq { position: absolute; left: 43px; top: 794px; width: 606px; }
  .faq .body-text { font-size: 13px; text-align: left; }
  .faq .heading + .body-text { margin-top: 6px; }
  .faq-block + .faq-block { margin-top: 25px; }
  .faq-block .body-text + .body-text { margin-top: 24px; }

  .footer { position: absolute; left: 0; top: 1147px; width: 692px; height: 53px; background: var(--footer);
    color: var(--white); font-weight: 700; font-size: 12.8px; display: flex; align-items: center; justify-content: center; }
  .footer .issue { position: absolute; right: 36px; }
</style>
</head>
<body>
<div class="newsletter">
  <header>
    <div class="brand"><span class="brand-dot"></span><span class="brand-name">HALVERD QUENBY</span></div>
    <a class="site-pill" href="https://www.halverd-quenby.com">
      <span class="globe">
        <svg width="18" height="18" viewBox="0 0 20 20" fill="none" stroke="#2b7f8a" stroke-width="1.6">
          <circle cx="10" cy="10" r="8"/><ellipse cx="10" cy="10" rx="3.5" ry="8"/><line x1="2" y1="10" x2="18" y2="10"/>
        </svg>
      </span>
      www.halverd-quenby.com
    </a>
  </header>

  <section class="main-col">
    <h2 class="heading">Confidentiality is the key</h2>
    <p class="body-text">We share your information with no one, period. Our founders have never been the founders of the CallPath Group. Our founders have never been members of the FCC. We have never been sued (or even inquired) by a state attorney general.</p>

    <h2 class="heading second">Using highly developed artificial<br>intelligence, machine learning,<br>analytics, database manipulation,<br>and human oversight</h2>
    <p class="sub-heading">we can tell you what is actually on your network.</p>
    <p class="body-text">Send 1% of your traffic, randomly, throughout the day, and we'll tell you what is really on your network. End Tracebacks, huge fines, and inquiries from the FCC and multiple states' AG.</p>
    <p class="body-text next">With the guidance of some of the best telecommunications attorneys in the nation, we keep this process legal meeting Federal privacy and wiretap regulations.</p>

    <p class="callout">WIth Nimbus's best partners on the Nimbus Cloud, we've developed monitoring that will find virtually all of fraud on your network, blatant TCPA and TSR violations.</p>
  </section>

  <aside class="news-box">
    <h2 class="news-title">LATEST NEWS</h2>
    <p class="news-item"><a href="#">Sed ut perspiciatis unde omnis iste natus error sit voluptatem accus an tium doloremque laudantium, totam</a></p>
    <p class="news-item"><a href="#">Sed ut perspiciatis unde omnis iste natus error sit voluptatem accus an tium doloremque laudantium, totam</a></p>
    <p class="news-item"><a href="#">Sed ut perspiciatis unde omnis iste natus error sit voluptatem</a></p>
    <p class="news-item"><a href="#">Perspiciatis unde omnis iste natus error sit voluptatem accus</a></p>
  </aside>

  <div class="feature-art" role="img" aria-label="Illustration of a glowing circuit-board brain with a hand reaching toward it"></div>

  <section class="faq">
    <div class="faq-block">
      <h2 class="heading">What happens when you find fraud on my network?</h2>
      <p class="body-text">We do NOT notify the CallPath Group, nor the FCC, nor the FTC, nor any Attorney General's office.</p>
    </div>
    <div class="faq-block">
      <h2 class="heading">What happens then?</h2>
      <p class="body-text">We put the fraud/TCPA notices, along with the sample recording, in your on-line portal for your<br>review.</p>
      <p class="body-text">We urge you to then contact your call producers to remove the fraud or TCPA violations.</p>
    </div>
    <div class="faq-block">
      <h2 class="heading">And more?</h2>
      <p class="body-text">As we are focused on fraud and obvious TCPA violations, we give you additional information to help you comply with STIR/SHAKEN regulations, such as the attestation level of toKENs attached to the fraud calls, a scrub against the Do-Not-Cal list and a scrub against our internal Do-Not-Originate list.</p>
    </div>
  </section>

  <footer class="footer">(C) Copyright 2024 | All Rights Reserved<span class="issue">C58</span></footer>
</div>
</body>
</html>
```